Coffee and fruit juice

We are a Kedai Sentosa that also serves aussie coffee and breakfast from 7am to 11am. After 11am we serve malaysian food but we also have a salad and sandwhich bar for people to choose from. We need a poster to hang outside our door to let people know that we are now also serving aussie coffee and breakfast as well as our usual malaysian cuisine.

Target Market(s)

Office location

Industry/Entity Type

Restaurant

Font styles to use
Decorative
Script

Requirements
Must have
• images and word
Nice to have
• something bold to attract people's attention

```html
<!DOCTYPE html>
<html lang="en">
<head>
<meta charset="utf-8">
<title>Kedai Sentosa – Now Open Poster</title>
<link href="https://fonts.googleapis.com/css2?family=Anton&family=Arimo:wght@400;700&family=Tinos:ital,wght@1,700&display=swap" rel="stylesheet">
<style>
  :root {
    --page: #ffffff;
    --orange-dark: #a8230a;
    --orange-light: #ee6e08;
    --yellow: #ffe000;
    --yellow-light: #ffd200;
    --brown: #3a1e14;
    --green-light: #a6c514;
    --green-dark: #4e8f1f;
    --brand-green: #1f8a3e;
    --accent-yellow: #f4e83a;
    --white: #ffffff;
    --black: #111111;
    --coffee-a: #6b2c1c;
    --coffee-b: #c9a27a;
    --juice-a: #1d56b0;
    --juice-b: #f2a81a;
    --meal-a: #f1ece4;
    --meal-b: #6b3418;
  }
  * { margin: 0; padding: 0; box-sizing: border-box; }
  html, body { width: 1200px; height: 1000px; overflow: hidden; background: var(--page); }
  .poster {
    position: absolute; left: 68px; top: 50px; width: 1060px; height: 750px;
    border: 1.5px solid var(--black); overflow: hidden;
    font-family: "Arimo", Arial, sans-serif;
  }
  .block { position: absolute; }
  .opening {
    left: 0; top: 0; width: 349px; height: 235px;
    background: linear-gradient(135deg, var(--orange-dark), var(--orange-light));
    color: var(--white); text-align: center;
  }
  .opening__headline {
    font-family: "Anton", "Oswald", sans-serif; font-size: 78px; line-height: 1;
    margin-top: 44px; letter-spacing: 0.5px;
  }
  .opening__sub { font-size: 41px; margin-top: 12px; }
  .masthead {
    left: 349px; top: 0; width: 711px; height: 235px;
    background: linear-gradient(90deg, var(--yellow-light), var(--yellow));
  }
  .brand { position: absolute; left: 26px; top: 52px; display: flex; align-items: center; }
  .brand__name {
    font-family: "Arimo", Arial, sans-serif; font-weight: 700; font-size: 46px;
    color: var(--brand-green); margin-left: 22px;
  }
  .badges { position: absolute; left: 492px; top: 14px; }
  .address {
    position: absolute; left: 470px; top: 140px; width: 200px; text-align: center;
    font-size: 16px; line-height: 19px; color: var(--black);
  }
  .menu {
    left: 0; top: 235px; width: 707px; height: 232px; background: var(--brown);
    color: var(--white);
  }
  .menu__item { position: absolute; text-align: center; }
  .menu__item--breakfast { left: 22px; top: 32px; width: 340px; }
  .menu__item--salad { left: 366px; top: 92px; width: 324px; }
  .menu__title { font-weight: 700; line-height: 1; }
  .menu__time {
    font-family: "Tinos", "Times New Roman", serif; font-style: italic; font-weight: 700;
    color: var(--accent-yellow);
  }
  .delivery {
    left: 707px; top: 235px; width: 353px; height: 232px;
    background: linear-gradient(135deg, var(--green-light), var(--green-dark));
    color: var(--black); text-align: center;
  }
  .delivery__label { font-size: 28px; margin-top: 62px; }
  .delivery__phone { font-size: 41px; font-weight: 700; margin-top: 10px; }
  .photo { top: 467px; height: 283px; }
  .photo--coffee { left: 0; width: 349px; background: radial-gradient(circle at 45% 45%, var(--coffee-b), var(--coffee-a)); }
  .photo--juice { left: 349px; width: 358px; background: linear-gradient(180deg, var(--juice-a) 0%, var(--juice-b) 75%, #ffffff 100%); }
  .photo--meal { left: 707px; width: 353px; background: linear-gradient(100deg, var(--meal-a) 30%, var(--meal-b) 85%); }
</style>
</head>
<body>
  <main class="poster">
    <section class="block opening">
      <div class="opening__headline">NOW OPEN</div>
      <div class="opening__sub">TO SERVE YOU</div>
    </section>

    <header class="block masthead">
      <div class="brand">
        <svg width="120" height="120" viewBox="0 0 120 120" aria-hidden="true">
          <circle cx="60" cy="60" r="54" fill="none" stroke="var(--brand-green)" stroke-width="10"/>
        </svg>
        <span class="brand__name">Kedai Sentosa</span>
      </div>
      <svg class="badges" width="200" height="80" viewBox="0 0 200 80" aria-label="Certification and amenity badges">
        <circle cx="38" cy="36" r="36" fill="var(--black)"/>
        <circle cx="38" cy="36" r="30" fill="var(--yellow)"/>
        <rect x="94" y="10" width="100" height="52" rx="26" fill="var(--black)"/>
      </svg>
      <p class="address">Your address here,<br>yourCity, Malaysia</p>
    </header>

    <section class="block menu">
      <div class="menu__item menu__item--breakfast">
        <div class="menu__title" style="font-size:36px;">USSIE COFFEE &amp;</div>
        <div class="menu__title" style="font-size:54px;">BREAKFAST</div>
        <div class="menu__time" style="font-size:28px; margin-top:8px;">from 7am to 11am</div>
      </div>
      <div class="menu__item menu__item--salad">
        <div class="menu__title" style="font-size:48px; letter-spacing:6px;">SALAD &amp;</div>
        <div class="menu__title" style="font-size:29px; margin-top:2px;">SANDWHICH BAR</div>
        <div class="menu__time" style="font-size:29px; margin-top:8px;">After 11am available</div>
      </div>
    </section>

    <section class="block delivery">
      <div class="delivery__label">Free Home Delivery</div>
      <div class="delivery__phone">(0198) 765432</div>
    </section>

    <div class="block photo photo--coffee" role="img" aria-label="Photo of a latte with leaf latte art in a white cup"></div>
    <div class="block photo photo--juice" role="img" aria-label="Photo of orange juice being poured into a glass"></div>
    <div class="block photo photo--meal" role="img" aria-label="Photo of a Malaysian rice plate with rendang and sides"></div>
  </main>
</body>
</html>
```